Looking for a full stationery set design for our business - NO generic/stock templates please.

I am looking for a complete stationary set for my used car dealership. I am looking for something, unique, creative, classy and high-end. Generic designs or anything that looks like a 'stock' template will not be selected. Please do not use a vehicle image in the design - - that is too predictable for a car dealership.

I prefer matte designs over shiny/glossy designs but will consider both if the look is right. I have attached a few different variations of our logo you can work with, as well as a QR code to our website.

These are the items needed:
- Letterhead (with MS word file)
- Envelope #10
- Envelope 9" x 12"
- Envelope 10" x 13"
- Presentation Folder 9" x 12"
- Business Cards 2" x 3.5"
- Folded Card (5.5 x 8" folded to 4" x 5.5")
- Notepad Small (4" x 6")
- Notepad Large (5.5" x 8.5")
- Postcard (4" x 6")

Low design entries Many entries from the same designers Many repetitive designs Too many generic entries that look like stock templates

• Original, creative work, high-end/classy appeal. Must stand out as high-quality, professional image that captures your attention.
• No generic/stock templates or anything that looks like it.

```html
<!DOCTYPE html>
<html lang="en">
<head>
<meta charset="utf-8">
<title>Harbor Motor Works – Presentation Folder</title>
<link rel="stylesheet" href="https://fonts.googleapis.com/css2?family=Roboto:wght@400;700;900&display=swap">
<style>
  :root {
    --stage: #c9c8c9;
    --brand-blue: #1a80c2;
    --brand-blue-deep: #135e92;
    --ink-dark: #333335;
    --paper: #ffffff;
    --paper-shade: #dcdcdc;
    --text-light: #ffffff;
  }
  * { margin: 0; padding: 0; box-sizing: border-box; }
  html, body {
    width: 1200px;
    height: 847px;
    overflow: hidden;
    background: var(--stage);
    font-family: "Roboto", Arial, sans-serif;
  }
  .canvas {
    position: relative;
    width: 1200px;
    height: 847px;
    display: flex;
    justify-content: center;
    align-items: center;
  }
  .folder-spread {
    display: flex;
    width: 840px;
    height: 560px;
  }
  .folder-panel {
    position: relative;
    width: 420px;
    height: 560px;
    overflow: hidden;
  }
  .folder-back {
    background: linear-gradient(90deg, var(--brand-blue-deep) 0%, var(--brand-blue) 40%, var(--brand-blue) 55%, var(--brand-blue-deep) 100%);
  }
  .contact-block {
    position: absolute;
    left: 0;
    right: 0;
    bottom: 70px;
    text-align: center;
    color: var(--text-light);
    font-size: 11.5px;
    line-height: 1.45;
    letter-spacing: 0.3px;
  }
  .contact-company {
    font-weight: 700;
    font-size: 12px;
  }
  .contact-line svg {
    width: 11px;
    height: 9px;
    vertical-align: -1px;
    margin: 0 3px;
  }
  .folder-front {
    background: linear-gradient(135deg, var(--paper) 0%, var(--paper) 45%, var(--paper-shade) 100%);
  }
  .brand-name {
    position: absolute;
    top: 170px;
    left: 0;
    right: 0;
    text-align: center;
    font-weight: 900;
    font-size: 34px;
    letter-spacing: 0.5px;
    color: var(--brand-blue);
    line-height: 1.1;
  }
  .front-band {
    position: absolute;
    left: 0;
    bottom: 0;
    width: 420px;
    height: 60px;
  }
  .band-web {
    position: absolute;
    left: 300px;
    right: 0;
    bottom: 11px;
    text-align: center;
    color: var(--text-light);
    font-size: 10.5px;
    line-height: 1;
    letter-spacing: 0.5px;
  }
</style>
</head>
<body>
<main class="canvas">
  <section class="folder-spread">
    <div class="folder-panel folder-back">
      <div class="contact-block">
        <p class="contact-company">Harbor Motor Works Ltd.</p>
        <p class="contact-line">48 Alder Crest Road, Lakeview, ON K2P 4M1</p>
        <p class="contact-line">
          <svg viewBox="0 0 12 10" aria-hidden="true"><path d="M1 3 Q6 -1 11 3 L10 4.5 L8 4 L8 3 Q6 2 4 3 L4 4 L2 4.5 Z M2.5 5 L9.5 5 L10.5 9.5 L1.5 9.5 Z" fill="#fff"/></svg>555.204.7788
          <svg viewBox="0 0 12 9" aria-hidden="true"><rect x="0.5" y="0.5" width="11" height="8" fill="none" stroke="#fff"/><path d="M0.5 0.5 L6 5 L11.5 0.5" fill="none" stroke="#fff"/></svg>info@harbormotor.com
        </p>
        <p class="contact-line">www.harbormotor.com</p>
      </div>
    </div>
    <div class="folder-panel folder-front">
      <h1 class="brand-name">Harbor Motor Works</h1>
      <svg class="front-band" viewBox="0 0 420 60" aria-hidden="true">
        <path d="M0 50 L270 50 Q282 50 288 40 Q294 28 306 28 L420 28 L420 60 L0 60 Z" fill="var(--brand-blue)"/>
        <path d="M0 43 L266 43 Q276 43 281 34 Q288 20 302 20 L420 20 L420 23 L304 23 Q291 23 285 36 Q279 46 266 46 L0 46 Z" fill="var(--ink-dark)"/>
      </svg>
      <span class="band-web">www.harbormotor.com</span>
    </div>
  </section>
</main>
</body>
</html>
```